bright frame masters

we are a window and door installation company for residential and commercial buildings

These cards are for Colin Mercer
His email is colin@brightframemastersco.com and he is a project manager.

Are colors are white red and black

I want all of his information on the card and a few pictures of windows and doors

```html
<!DOCTYPE html>
<html lang="en">
<head>
<meta charset="utf-8">
<title>Bright Frame Masters – Business Card</title>
<link rel="stylesheet" href="https://fonts.googleapis.com/css2?family=Libre+Baskerville:wght@700&family=Poppins:wght@400&display=swap">
<style>
  :root {
    --brand-red: #a3173a;
    --ink: #1a1a1a;
    --paper: #ffffff;
    --backdrop: #2b2b2b;
  }
  * { box-sizing: border-box; margin: 0; padding: 0; }
  html, body { width: 1189px; height: 1200px; overflow: hidden; }
  body { background: var(--backdrop); position: relative; font-family: "Poppins", sans-serif; }

  .card {
    position: absolute;
    left: 171px;
    width: 857px;
    height: 490px;
    background: var(--paper);
    box-shadow: 0 6px 18px rgba(0,0,0,.45);
    overflow: hidden;
  }
  .card--front { top: 66px; }
  .card--back { top: 625px; }

  .company { position: absolute; left: 0; top: 58px; width: 440px; text-align: center;
    font-family: "Libre Baskerville", serif; font-weight: 700; color: var(--brand-red); }
  .company__name { font-size: 27px; letter-spacing: .3px; line-height: 1; }
  .company__tagline { font-size: 12px; margin-top: 9px; letter-spacing: .4px; }
  .company__phone { font-size: 20px; margin-top: 8px; }

  .namebox { position: absolute; left: 545px; top: 57px; width: 312px; height: 73px;
    background: var(--brand-red); color: var(--paper); padding: 10px 0 0 37px; }
  .namebox__name { font-family: "Libre Baskerville", serif; font-weight: 700; font-size: 21px; line-height: 1.2; }
  .namebox__role { font-size: 16px; margin-top: 3px; }

  .gallery { position: absolute; left: 0; top: 200px; width: 857px; height: 215px; background: var(--brand-red); }
  .gallery__photo { position: absolute; top: 7px; height: 202px; width: 206px; }
  .gallery__photo--folding { left: 6px; background: linear-gradient(180deg,#e8ebee 0%,#b9c9a8 45%,#6f8c4b 75%,#3a2a20 100%); }
  .gallery__photo--shower { left: 219px; background: linear-gradient(135deg,#f2f2f2 0%,#d8dcdf 55%,#b08460 100%); }
  .gallery__photo--office { left: 432px; background: linear-gradient(180deg,#6f9bd2 0%,#c9d6e4 40%,#8aa2b6 75%,#6a6e66 100%); }
  .gallery__photo--patio { left: 645px; background: linear-gradient(90deg,#c98a3f 0%,#e9e2cf 15%,#5f8a3a 50%,#e9e2cf 85%,#c98a3f 100%); }

  .contact { position: absolute; top: 436px; left: 0; width: 857px; height: 32px; color: var(--ink); font-size: 21px; }
  .contact__item { position: absolute; top: 0; display: flex; align-items: center; gap: 10px; line-height: 32px; }
  .contact__item--phone { left: 47px; }
  .contact__item--email { left: 385px; top: -3px; }
  .contact__icon { width: 25px; height: 25px; flex: none; }
  .contact__divider { position: absolute; left: 313px; top: 0; width: 2px; height: 32px; background: var(--brand-red); }

  .website { position: absolute; top: 230px; left: 0; width: 857px; height: 30px; }
  .website__rule { position: absolute; top: 14px; height: 2px; background: var(--ink); width: 126px; }
  .website__rule--left { left: 0; }
  .website__rule--right { right: 0; }
  .website__url { position: absolute; left: 0; right: 0; text-align: center; color: var(--brand-red);
    font-size: 25px; letter-spacing: 3.2px; line-height: 30px; }
</style>
</head>
<body>
  <section class="card card--front">
    <div class="company">
      <div class="company__name">BRIGHT FRAME MASTERS</div>
      <div class="company__tagline">RESIDENTAL &amp; COMMERCIAL</div>
      <div class="company__phone">(555) 214-0387</div>
    </div>

    <div class="namebox">
      <div class="namebox__name">COLIN MERCER</div>
      <div class="namebox__role">Project Manager</div>
    </div>

    <div class="gallery">
      <div class="gallery__photo gallery__photo--folding" role="img" aria-label="Photo of open folding glass doors leading to a garden"></div>
      <div class="gallery__photo gallery__photo--shower" role="img" aria-label="Photo of a frameless glass shower enclosure"></div>
      <div class="gallery__photo gallery__photo--office" role="img" aria-label="Photo of a commercial building with glass window walls"></div>
      <div class="gallery__photo gallery__photo--patio" role="img" aria-label="Photo of grid patio doors and windows opening to a yard"></div>
    </div>

    <div class="contact">
      <div class="contact__item contact__item--phone">
        <svg class="contact__icon" viewBox="0 0 24 24" aria-hidden="true">
          <circle cx="12" cy="12" r="12" fill="var(--brand-red)"/>
          <path d="M6 10.5c0-2 2.5-3 6-3s6 1 6 3l-2 .8-1.2-1.8h-5.6L8 11.3z" fill="#fff"/>
          <rect x="7.5" y="12" width="9" height="5" rx="1" fill="#fff"/>
          <circle cx="12" cy="14.5" r="1.3" fill="var(--brand-red)"/>
        </svg>
        <span>555-318-2046</span>
      </div>
      <div class="contact__divider"></div>
      <div class="contact__item contact__item--email">
        <svg class="contact__icon" viewBox="0 0 24 24" aria-hidden="true">
          <circle cx="12" cy="12" r="12" fill="var(--brand-red)"/>
          <rect x="6" y="8" width="12" height="8.5" rx="1" fill="none" stroke="#fff" stroke-width="1.4"/>
          <path d="M6.5 8.7 12 13l5.5-4.3" fill="none" stroke="#fff" stroke-width="1.4"/>
        </svg>
        <span>colin@brightframemastersco.com</span>
      </div>
    </div>
  </section>

  <section class="card card--back">
    <div class="website">
      <span class="website__rule website__rule--left"></span>
      <div class="website__url">WWW.BRIGHTFRAMEMASTERSCO.COM</div>
      <span class="website__rule website__rule--right"></span>
    </div>
  </section>
</body>
</html>
```